Landscaping Carbonless Copy Door to Door Sales Order Form

I need an order form created for my landscaping company. It will be used when we go door to door to make sales. This form will be used as a two part carbon-less copy form, so that when we write on the form at the door of a prospective customer we both can keep a copy of the information. The first file attached is a copy of a competitors form and sort of an example of how I would like ours to look. The second file is the writing that I want to incorporate on mine, since it will be a little different than the competitors services. It is not exactly how I want it to look so feel free to rearrange things to look good. I believe how the first example has it, the areas in which we will write things in will be white, and the surrounding areas will be colored. Green is good for the main color scheme. The third file will be the logo I want attached. I have the logo in various other files if you need.

Target Market(s)

Upscale Residential

Industry/Entity Type

Landscaping

Font styles to use
Sans Serif

Colors
9bcb3c

Requirements
Must have
• Logo, address, phone number, website, usable table for completing sales.
• The two main plan options should have a box you can check to receive and then a box to write in the price for prepaid and the price per visit. The additional services should also have a small box next to them so that you can check to receive, notes should also be in a box, remember this is an order form and needs to be functional, look to the example as a guide.
Nice to have
• Area to take notes and add extras, if you need to fill in more space you can put a referral box and offer to recieve 50 credit to your account for referring a paid customer.
Should not have
• a Cheap look

```html
<!DOCTYPE html>
<html lang="en">
<head>
<meta charset="utf-8">
<title>Fernleaf Lawn &amp; Landscape — Sales Order Form</title>
<link rel="stylesheet" href="https://fonts.googleapis.com/css2?family=Montserrat:wght@400;500;600;700;800&display=swap">
<style>
  :root{
    --leaf:#9bcb3c;
    --leaf-light:#c3e06a;
    --forest:#3f8a2e;
    --deep:#1f5a24;
    --grass-dark:#2f6d1f;
    --grass-mid:#4e9a2c;
    --title-yellow:#f2e54b;
    --ink:#2a2a2a;
    --paper:#ffffff;
    --rule:#4a4a4a;
    --backdrop:#eeeeea;
  }
  *{box-sizing:border-box;margin:0;padding:0}
  html,body{width:993px;height:1200px;overflow:hidden;background:var(--backdrop)}
  body{font-family:"Montserrat",Arial,sans-serif;color:var(--ink)}

  .order-form{position:relative;width:993px;height:1200px;background:var(--paper);overflow:hidden}

  .grass-field{position:absolute;left:0;top:215px;width:993px;height:905px;
    background:radial-gradient(ellipse at 30% 40%,var(--grass-mid),var(--grass-dark) 75%)}
  .grass-fringe{position:absolute;left:0;top:190px;width:993px;height:40px;
    background:linear-gradient(180deg,rgba(255,255,255,0),rgba(78,154,44,.55) 60%,var(--grass-mid))}

  .company-contact{position:absolute;left:56px;top:92px}
  .company-contact .phone{font-size:38px;font-weight:700;color:var(--deep);letter-spacing:.5px}
  .company-contact .line{font-size:16px;font-weight:500;color:var(--deep);margin-top:4px}

  .brand{position:absolute;left:420px;top:96px;display:flex;align-items:center;gap:12px}
  .brand .mark{width:40px;height:40px;border-radius:50%;background:var(--leaf)}
  .brand .name{font-size:30px;font-weight:800;color:var(--forest);line-height:1}
  .brand .sub{font-size:11px;font-weight:700;color:var(--forest);letter-spacing:2px;margin-top:4px}

  .prepay-tab{position:absolute;right:40px;top:40px;width:200px;padding:12px 16px;
    background:linear-gradient(180deg,var(--leaf-light),var(--leaf));color:#fff;border-radius:6px;text-align:center}
  .prepay-tab .small{font-size:14px;font-weight:600;letter-spacing:1px}
  .prepay-tab .big{font-size:36px;font-weight:800;line-height:1}

  .customer-card{position:absolute;left:50px;top:240px;width:893px;height:228px;background:var(--paper);padding:26px 34px}
  .field-row{display:flex;gap:22px;margin-bottom:24px}
  .field{display:flex;align-items:flex-end;flex:1;font-size:15px;font-weight:500}
  .field span{white-space:nowrap;margin-right:6px}
  .field i{flex:1;border-bottom:1px solid var(--rule);height:18px}
  .field.narrow{flex:.55}

  .panel{position:absolute;border-radius:10px;overflow:hidden;background:linear-gradient(180deg,var(--leaf-light),var(--leaf) 70%,#8bbd30)}
  .panel-title{display:inline-block;background:var(--deep);color:var(--title-yellow);
    font-size:24px;font-weight:700;padding:6px 22px;border-radius:0 0 8px 0}

  .plan-options{left:50px;top:486px;width:893px;height:218px}
  .plan-list{list-style:none;padding:14px 30px 0;width:560px}
  .plan-list li{display:flex;gap:14px;margin-bottom:10px}
  .check-box{flex:none;width:18px;height:18px;background:#fff;border:1px solid var(--deep);margin-top:2px}
  .plan-list strong{display:block;font-size:19px;font-weight:700;color:var(--deep);line-height:1.3}
  .plan-list em{display:block;font-style:normal;font-size:13px;line-height:1.4;font-weight:500;color:#26461c}
  .price-boxes{position:absolute;right:24px;top:18px;display:flex;gap:14px}
  .price-box{width:140px;height:180px;background:#fff;border-radius:4px;padding:8px;font-size:12px;font-weight:700;color:var(--deep)}

  .additional-services{left:50px;top:722px;width:490px;height:380px}
  .service-list{list-style:none;padding:16px 24px 0}
  .service-list li{display:flex;gap:12px;font-size:14px;font-weight:600;color:var(--deep);margin-bottom:11px;line-height:1.3}
  .service-list .check-box{width:16px;height:16px;margin-top:1px}

  .notes-card{position:absolute;left:558px;top:722px;width:385px;height:380px;background:var(--paper);
    border-radius:10px;padding:22px 24px}
  .notes-card .label{font-size:16px;font-weight:700}
  .notes-lines i{display:block;border-bottom:1px solid var(--rule);height:28px}
  .sign-row{margin-top:22px}
  .sign-row .field{margin-bottom:16px}
  .terms{font-size:9px;line-height:1.35;color:#444;margin-top:6px}

  .contact-bar{position:absolute;left:0;bottom:0;width:993px;height:80px;background:var(--deep);
    color:#fff;display:flex;align-items:center;justify-content:center;gap:18px;font-size:19px;font-weight:500}
  .contact-bar .sep{opacity:.6}
</style>
</head>
<body>
<main class="order-form">
  <div class="grass-field" role="img" aria-label="Close-up photograph of green lawn grass"></div>
  <div class="grass-fringe" role="img" aria-label="Grass blades along the header edge"></div>

  <header>
    <div class="company-contact">
      <div class="phone">555-014-2273</div>
      <div class="line">PO Box 12 Ashdale IL 60000</div>
      <div class="line">www.fernleafyards.com</div>
    </div>
    <div class="brand">
      <div class="mark"></div>
      <div>
        <div class="name">Fernleaf</div>
        <div class="sub">LAWN &amp; LANDSCAPE</div>
      </div>
    </div>
    <div class="prepay-tab">
      <div class="small">PRE PAY &amp; SAVE</div>
      <div class="big">10% OFF</div>
    </div>
  </header>

  <section class="customer-card">
    <div class="field-row"><div class="field"><span>Name:</span><i></i></div></div>
    <div class="field-row"><div class="field"><span>Address:</span><i></i></div></div>
    <div class="field-row">
      <div class="field"><span>City:</span><i></i></div>
      <div class="field narrow"><span>Zip:</span><i></i></div>
    </div>
    <div class="field-row">
      <div class="field"><span>Telephone:</span><i></i></div>
      <div class="field narrow"><span>Rep:</span><i></i></div>
      <div class="field narrow"><span>Date:</span><i></i></div>
    </div>
  </section>

  <section class="panel plan-options">
    <h2 class="panel-title">Plan Options</h2>
    <ul class="plan-list">
      <li><span class="check-box"></span><div><strong>Mow and Go Program</strong><em>(Edging of sidewalks and drives, trimming, blowing off debris; provided weekly unless no growth of grass due to drought)</em></div></li>
      <li><span class="check-box"></span><div><strong>Full Service Program</strong><em>(Weekly Lawn Mowing, Fertilization/Weed Control, 2 Bush Trimming, Spring/Fall Cleanups)</em></div></li>
    </ul>
    <div class="price-boxes">
      <div class="price-box">Monthly Price:</div>
      <div class="price-box">Prepaid Price:</div>
    </div>
  </section>

  <section class="panel additional-services">
    <h2 class="panel-title">Additional Services</h2>
    <ul class="service-list">
      <li><span class="check-box"></span>Fertilizing and Weed Control - 4 Treatments Core Aeration</li>
      <li><span class="check-box"></span>Bush and Tree Trimming</li>
      <li><span class="check-box"></span>Grub Control</li>
      <li><span class="check-box"></span>Spring Cleanup to Remove all leaves, debris, sticks, etc.</li>
      <li><span class="check-box"></span>Fall Cleanup to Remove all leaves, debris, sticks, etc.</li>
      <li><span class="check-box"></span>Weed Control in Beds (Spraying of weeds &amp; hand pulling large weeds, once per month)</li>
      <li><span class="check-box"></span>Snow Removal (Two inches or more, automatic dispatch)</li>
    </ul>
  </section>

  <section class="notes-card">
    <div class="label">Notes:</div>
    <div class="notes-lines"><i></i><i></i><i></i><i></i></div>
    <div class="sign-row">
      <div class="field"><span class="label">Print Name:</span><i></i></div>
      <div class="field"><span class="label">Signature:</span><i></i></div>
    </div>
    <p class="terms">By signing above I agree to use Fernleaf Lawn &amp; Landscape as my lawn care provider and pay in full for any services rendered. Service will continue each season until I cancel in writing. Unpaid balances after thirty days carry a late fee of 1.5% per month. Customer agrees to pay all reasonable collection costs and attorney fees incurred to collect any sums due under this contract.</p>
  </section>

  <footer class="contact-bar">
    <span>555-014-2273</span><span class="sep">|</span>
    <span>www.fernleafyards.com</span><span class="sep">|</span>
    <span>PO Box 12 Ashdale IL 60000</span>
  </footer>
</main>
</body>
</html>
```